Stationary design for panelrise

Dear Freelancer

Need a stationary desing for a panelrise company.
Business card (front & back), letterhead, envelope

Use the attached logo and adress
Regarding the design.... my client is a fan from http://www.harborlinemotors.example/

Need all source files incl. fonts.
Check my clients work with the following video:
http://www.vidstreamer.example/watch?v=pQ7mZt2XwBn

Best Regards
Gareth

```html
<!DOCTYPE html>
<html lang="en">
<head>
<meta charset="utf-8">
<title>Panelrise C5 Envelope Layout</title>
<link rel="stylesheet" href="https://fonts.googleapis.com/css2?family=Open+Sans:wght@400;600;700;800&display=swap">
<style>
  :root {
    --page: #f6f7f7;
    --paper: #ffffff;
    --ink: #1f1f1f;
    --dim: #222222;
    --orange: #f08a24;
    --yellow: #f9c21a;
    --red: #e8262b;
    --band: #1b1b1b;
    --clear: #eceeef;
    --grid: #dadddf;
    --outline: #3a3a3a;
  }
  html, body {
    margin: 0;
    padding: 0;
    width: 1200px;
    height: 1027px;
    overflow: hidden;
    background: var(--page);
  }
  .sheet {
    display: block;
    width: 1200px;
    height: 1027px;
    font-family: "Open Sans", Arial, sans-serif;
  }
  .dim-label { font-size: 21px; fill: var(--dim); font-weight: 400; }
  .clear-title { font-size: 18.5px; fill: var(--orange); }
  .clear-note { font-size: 18.5px; fill: var(--ink); }
  .brand-name { font-size: 58px; font-weight: 700; fill: var(--ink); letter-spacing: -1.5px; }
  .contact { font-size: 11.5px; font-weight: 600; fill: var(--ink); }
  .return-note { font-size: 12px; fill: var(--ink); }
  .size-code { font-size: 80px; font-weight: 800; fill: var(--orange); }
  .size-spec { font-size: 18.5px; fill: var(--ink); }
  .flap-label { font-size: 21px; fill: var(--ink); }
</style>
</head>
<body>
<svg class="sheet" viewBox="0 0 1200 1027" xmlns="http://www.w3.org/2000/svg">
  <defs>
    <marker id="arrow-head" viewBox="0 0 10 10" refX="9" refY="5" markerWidth="9" markerHeight="9" orient="auto-start-reverse">
      <path d="M0,1 L10,5 L0,9" fill="none" stroke="#222" stroke-width="1.4"/>
    </marker>
    <pattern id="clear-grid" width="18" height="18" patternUnits="userSpaceOnUse">
      <path d="M18 0 L0 0 0 18" fill="none" stroke="var(--grid)" stroke-width="1"/>
    </pattern>
  </defs>

  <!-- overall width dimension -->
  <g class="dimension width">
    <line x1="122" y1="73" x2="963" y2="73" stroke="var(--dim)" stroke-width="1.3" marker-start="url(#arrow-head)" marker-end="url(#arrow-head)"/>
    <rect x="500" y="58" width="80" height="30" fill="var(--page)"/>
    <text class="dim-label" x="540" y="81" text-anchor="middle">228mm</text>
  </g>

  <!-- overall height dimension -->
  <g class="dimension height">
    <line x1="91" y1="97" x2="91" y2="697" stroke="var(--dim)" stroke-width="1.3" marker-start="url(#arrow-head)" marker-end="url(#arrow-head)"/>
    <rect x="24" y="382" width="86" height="30" fill="var(--page)"/>
    <text class="dim-label" x="67" y="404" text-anchor="middle">162mm</text>
  </g>

  <!-- return flap -->
  <polygon class="flap" points="971,93 1101,167 1101,624 971,700" fill="var(--paper)" stroke="var(--outline)" stroke-width="1.3"/>
  <text class="return-note" transform="translate(1014 400) rotate(90)" text-anchor="middle">
    <tspan x="0" y="0">Return address</tspan>
    <tspan x="0" y="15">details,</tspan>
    <tspan x="0" y="30">if required.</tspan>
  </text>

  <!-- envelope face -->
  <rect class="envelope" x="113" y="93" width="858" height="607" fill="var(--paper)" stroke="var(--outline)" stroke-width="1.3"/>
  <rect class="clear-area" x="114" y="94" width="857" height="37" fill="var(--clear)"/>
  <rect class="clear-area-grid" x="114" y="94" width="857" height="37" fill="url(#clear-grid)"/>
  <line x1="114" y1="131" x2="971" y2="131" stroke="var(--orange)" stroke-width="1.3" stroke-dasharray="7 5"/>

  <!-- clear area note -->
  <g class="clear-note-group">
    <line x1="465" y1="178" x2="465" y2="139" stroke="var(--dim)" stroke-width="1.3" marker-end="url(#arrow-head)"/>
    <text class="clear-title" x="477" y="177">10mm clear area</text>
    <text class="clear-note" x="477" y="202">This edge is fed through the press first,</text>
    <text class="clear-note" x="477" y="230">so please leave a 10mm margin free of any artwork.</text>
  </g>

  <!-- brand name -->
  <text class="brand-name" x="153" y="275">panelrise</text>

  <!-- tri-colour rule -->
  <g class="header-rule">
    <rect x="144" y="305" width="264" height="5" fill="var(--yellow)"/>
    <rect x="408" y="305" width="261" height="5" fill="var(--orange)"/>
    <rect x="669" y="305" width="262" height="5" fill="var(--red)"/>
  </g>

  <!-- footer -->
  <line x1="144" y1="615" x2="931" y2="615" stroke="var(--orange)" stroke-width="2"/>
  <g class="contact-row">
    <text class="contact" x="151" y="639">Phone : +41(0)791234567</text>
    <text class="contact" x="349" y="639">Address : 123, address, City</text>
    <text class="contact" x="551" y="639">Email : mail@panelrise.example</text>
    <text class="contact" x="755" y="639">Website : www.panelrise.example</text>
  </g>
  <rect class="footer-accent" x="113" y="652" width="858" height="5" fill="var(--orange)"/>
  <rect class="footer-band" x="113" y="657" width="858" height="43" fill="var(--band)"/>

  <!-- fold line -->
  <line x1="971" y1="67" x2="971" y2="847" stroke="var(--orange)" stroke-width="1.3" stroke-dasharray="7 5"/>

  <!-- flap dimension -->
  <line x1="1101" y1="847" x2="1101" y2="645" stroke="var(--dim)" stroke-width="1.3" marker-end="url(#arrow-head)"/>
  <text class="flap-label" x="1035" y="771" text-anchor="middle">35mm</text>
  <text class="flap-label" x="1035" y="802" text-anchor="middle">flap</text>

  <!-- size specification -->
  <text class="size-code" x="163" y="790">C5</text>
  <text class="size-spec" x="312" y="749">Size:  without return address printed = 228mm x 162mm</text>
  <text class="size-spec" x="312" y="780">Size:  with return address printed = 263mm x 162mm</text>
</svg>
</body>
</html>
```